Business Card Design

we are a Business Training & Consulting company that specializes in Lean Six Sigma coaching & consulting. Our clients are Big Businesses and Consultancy firms. Need a card design that is minimalist and elegant.. need to feature logo of our KRV brand & probably at the back we also need to include the logo of the parent company (DORAMBE Business Group Pty. Ltd.)
Font needs to be consistent with our website font especially the KRV font on the website header.. (www.krvqa.example)
Hi All,
Industry/Entity Type
Business
Contact Information for Business Card
Marcus T Ellingrove
Director
Business Consultancy & Training Programs
www.krvqa.example
P.O. Box 5172,
Perth, Western Australia, 6164, Australia.
M: +61 4 5538 9071
T: 1 300 579 218
F: +61 8 9727 3185
marcus@krvqa.example
ABN # : 73 2951 807 36
ACN #: 295 180 736

```html
<!DOCTYPE html>
<html lang="en">
<head>
<meta charset="utf-8">
<title>KRV Business Cards</title>
<link href="https://fonts.googleapis.com/css2?family=Didact+Gothic&display=swap" rel="stylesheet">
<style>
  :root {
    --page-bg: #ffffff;
    --card-bg: #ffffff;
    --band-top: #0b3457;
    --band-bottom: #0f6d95;
    --ink-light: #eef5fa;
    --brand-blue: #0d4a78;
    --brand-accent: #1a8cc8;
    --card-shadow: rgba(0, 0, 0, 0.45);
  }
  * { margin: 0; padding: 0; box-sizing: border-box; }
  html, body {
    width: 1200px;
    height: 765px;
    overflow: hidden;
    background: var(--page-bg);
    font-family: "Didact Gothic", "Century Gothic", sans-serif;
  }
  .canvas { position: relative; width: 1200px; height: 765px; }

  .card {
    position: absolute;
    width: 569px;
    height: 331px;
    background: var(--card-bg);
    box-shadow: 3px 5px 12px var(--card-shadow);
    overflow: hidden;
  }
  .card--front { left: 96px; top: 74px; z-index: 2; }
  .card--back  { left: 539px; top: 357px; height: 313px; z-index: 1; }

  .brand {
    position: absolute;
    left: 0; right: 0;
    display: flex;
    align-items: center;
    justify-content: center;
    gap: 14px;
    color: var(--brand-blue);
    letter-spacing: 0.12em;
  }
  .brand__dot {
    width: 22px; height: 22px;
    border-radius: 50%;
    background: var(--brand-accent);
  }
  .card--front .brand { top: 90px; font-size: 58px; }
  .card--back .brand { top: 36px; font-size: 48px; }
  .card--back .brand__dot { width: 18px; height: 18px; }

  .parent-name {
    position: absolute;
    top: 175px; left: 0; right: 0;
    text-align: center;
    font-size: 14px;
    color: var(--brand-blue);
  }

  .band {
    position: absolute;
    left: 0; right: 0; bottom: 0;
    background: linear-gradient(to bottom, var(--band-top), var(--band-bottom));
    color: var(--ink-light);
    font-size: 13.5px;
    line-height: 18px;
  }
  .card--front .band { top: 244px; }
  .card--back .band { top: 226px; }

  .band__col { position: absolute; top: 12px; }
  .card--front .identity { left: 23px; }
  .card--front .contact { left: 321px; }
  .card--back .address { left: 55px; top: 14px; }
  .card--back .registration { right: 62px; top: 14px; text-align: right; }
</style>
</head>
<body>
<main class="canvas">

  <section class="card card--front" aria-label="Business card front">
    <div class="brand"><span class="brand__dot"></span><span class="brand__name">KRV</span></div>
    <div class="band">
      <div class="band__col identity">
        <p class="person-name">Marcus T Ellingrove</p>
        <p class="person-title">Director</p>
        <p class="person-dept">Business Consultancy &amp; Training Programs</p>
      </div>
      <div class="band__col contact">
        <p>M: +61 4 5538 9071</p>
        <p>T: 1 300 579 218 &nbsp;F: +61 8 9727 3185</p>
        <p>E: marcus@krvqa.example &nbsp;W: www.krvqa.example</p>
      </div>
    </div>
  </section>

  <section class="card card--back" aria-label="Business card back">
    <div class="brand"><span class="brand__dot"></span><span class="brand__name">KRV</span></div>
    <p class="parent-name">DORAMBE Business Group Pty. Ltd</p>
    <div class="band">
      <div class="band__col address">
        <p>P.O. Box 5172, Perth,</p>
        <p>Western Australia, 6164, Australia.</p>
      </div>
      <div class="band__col registration">
        <p>ABN # : 73 2951 807 36</p>
        <p>ACN #: 295 180 736</p>
      </div>
    </div>
  </section>

</main>
</body>
</html>
```